Broadcaster,Conference Host,Facilitator

Looking for a business card and logo to create the Grant Ollerby brand .. Something with a slant towards radio and conference speaking
I like the idea of classic black white or grey but open to suggestions

Target Market(s)

Corporates

Industry/Entity Type

Business

Contact Information for Business Card

Grant Ollerby
Email : Grant.Ollerby@fenmail.co.uk
Mobile : +44 7700 384216
Twitter : @Grantollerby

Font styles to use
Serif
Decorative
Script

Requirements
Must have
• Feel classy and dynamic
Should not have
• Cartoons

```html
<!DOCTYPE html>
<html lang="en">
<head>
<meta charset="utf-8">
<title>Grant Ollerby Voice – Business Card</title>
<link rel="stylesheet" href="https://fonts.googleapis.com/css2?family=Josefin+Sans:wght@400&family=Open+Sans:wght@400&display=swap">
<style>
  :root {
    --page-bg: #e4e4e2;
    --card-bg: #f2f2f0;
    --card-edge: #b9b9b7;
    --ink: #111111;
    --mark-tone: #cfcfcd;
  }
  html, body {
    margin: 0;
    padding: 0;
    width: 1200px;
    height: 970px;
    overflow: hidden;
    background: var(--page-bg);
  }
  .canvas {
    position: relative;
    width: 1200px;
    height: 970px;
  }
  .business-card {
    position: absolute;
    left: 173px;
    top: 270px;
    width: 854px;
    height: 476px;
    background: var(--card-bg);
    border: 1.5px solid var(--card-edge);
    border-radius: 24px;
    box-sizing: border-box;
    color: var(--ink);
  }
  .brand-mark-area {
    position: absolute;
    left: 341px;
    top: 31px;
    width: 171px;
    height: 171px;
    border-radius: 50%;
    background: var(--mark-tone);
  }
  .brand-name {
    position: absolute;
    left: 0;
    right: 0;
    top: 212px;
    margin: 0;
    text-align: center;
    font-family: "Josefin Sans", sans-serif;
    font-weight: 400;
    font-size: 52px;
    line-height: 1;
    letter-spacing: 0.5px;
    text-transform: uppercase;
  }
  .brand-tagline {
    position: absolute;
    left: 0;
    right: 0;
    top: 266px;
    display: flex;
    justify-content: center;
    align-items: center;
    gap: 22px;
    font-family: "Josefin Sans", sans-serif;
    font-size: 25px;
    letter-spacing: 7px;
    line-height: 1;
  }
  .tagline-rule {
    width: 99px;
    height: 2px;
    background: var(--ink);
  }
  .tagline-text { margin-right: -7px; }
  .contact {
    font-family: "Open Sans", sans-serif;
    font-size: 20px;
    line-height: 1;
  }
  .contact-email-icon {
    position: absolute;
    left: 415px;
    top: 345px;
    width: 23px;
    height: 23px;
  }
  .contact-email {
    position: absolute;
    left: 0;
    right: 0;
    top: 370px;
    text-align: center;
  }
  .contact-row {
    position: absolute;
    left: 0;
    right: 0;
    top: 406px;
    display: flex;
    justify-content: center;
    align-items: center;
    gap: 8px;
  }
  .contact-row svg { width: 25px; height: 25px; }
  .contact-divider {
    width: 1.5px;
    height: 35px;
    background: var(--ink);
    margin: 0 4px;
  }
</style>
</head>
<body>
<div class="canvas">
  <div class="business-card">
    <div class="brand-mark-area" role="img" aria-label="Brand mark area"></div>

    <h1 class="brand-name">Grant Ollerby</h1>
    <div class="brand-tagline">
      <span class="tagline-rule"></span>
      <span class="tagline-text">VOICE</span>
      <span class="tagline-rule"></span>
    </div>

    <svg class="contact-email-icon" viewBox="0 0 26 26" aria-label="Email">
      <circle cx="13" cy="13" r="12" fill="none" stroke="var(--ink)" stroke-width="2"/>
      <rect x="7" y="8.5" width="12" height="9" fill="none" stroke="var(--ink)" stroke-width="1.6"/>
      <path d="M7 8.5 L13 13.5 L19 8.5" fill="none" stroke="var(--ink)" stroke-width="1.6"/>
    </svg>
    <div class="contact contact-email">grant.ollerby@fenmail.co.uk</div>

    <div class="contact contact-row">
      <span class="contact-phone">+44 7700 384216</span>
      <svg viewBox="0 0 27 27" aria-label="Phone">
        <circle cx="13.5" cy="13.5" r="12.5" fill="none" stroke="var(--ink)" stroke-width="2"/>
        <path d="M7 11 Q13.5 6 20 11 L18 13 L16 11.5 L11 11.5 L9 13 Z" fill="var(--ink)"/>
        <rect x="8.5" y="13.5" width="10" height="6" rx="1" fill="var(--ink)"/>
      </svg>
      <span class="contact-divider"></span>
      <svg viewBox="0 0 27 27" aria-hidden="true">
        <circle cx="13.5" cy="13.5" r="12.5" fill="none" stroke="var(--ink)" stroke-width="2"/>
      </svg>
      <span class="contact-handle">@Grantollerby</span>
    </div>
  </div>
</div>
</body>
</html>
```